Business card for denture clinic Gumlyssa

We need a new business card with our new logo. We are a denture clinic in New Zealand with our target market being 45+ years old. We would need a space on the back to write our patients next appointment on. We would space for only one appointment rather than a list. We will attach a photo showing an example of this. But of course, we would like to see your twist on this. We want it to be bold and easy to read and a good mixture of professional but modern. We have attached our logo to be used on the card.

Target Market(s)

People aged 45+ needing dentures

Industry/Entity Type

Dental

Contact Information for Business Card

We want our logo on the front and the space to write an appointment on the back. I've attached an example our our old business card showing this. We need to have the technicians details on the front.

Font styles to use
Sans Serif

Colors
0255a3
919191
fbfbfb

Requirements
Must have
• The following details:
• Ravi Pelling BDT, PGDipCDentTech Marlow
• Dental Prosthetist
• Phone numbers: 0800 47 2150
• 09 571 3294
• Email: ravi@gumlyssa.co.nz
• www.gumlyssa.co.nz
• Address: 418 Whiroa Road
• Kauriwhenua East
• Auckland 0742
Nice to have
• We would like our business cards to have more than just two colours as we want them to be more vibrant. We have uploaded an example of a business card we liked that showed this.

```html
<!DOCTYPE html>
<html lang="en">
<head>
<meta charset="utf-8">
<title>Gumlyssa Business Card</title>
<link rel="stylesheet" href="https://fonts.googleapis.com/css2?family=Karla:wght@400;500;700&display=swap">
<style>
  :root {
    --brand-blue: #0255a3;
    --band-blue: #1170b8;
    --swoosh-grey: #c4c4c4;
    --text-grey: #919191;
    --paper: #fbfbfb;
    --card-white: #ffffff;
    --backdrop: #e9e6e1;
    --line-grey: #9a9a9a;
  }
  * { box-sizing: border-box; margin: 0; padding: 0; }
  html, body {
    width: 1200px; height: 1200px; overflow: hidden;
    background: var(--backdrop);
    font-family: "Karla", Arial, sans-serif;
  }
  .sheet {
    width: 1200px; height: 1200px;
    display: flex; flex-direction: column; align-items: center; justify-content: center;
    gap: 60px;
  }
  .card {
    position: relative;
    width: 800px; height: 488px;
    background: var(--card-white);
    box-shadow: 0 6px 18px rgba(0,0,0,0.12);
    overflow: hidden;
  }
  .card__band { position: absolute; inset: 0; width: 100%; height: 100%; }

  .brand { display: flex; align-items: center; gap: 18px; }
  .brand__square { background: var(--brand-blue); flex: none; }
  .brand__name {
    font-weight: 700; color: var(--brand-blue);
    text-transform: uppercase; letter-spacing: 0.04em; line-height: 1;
  }

  .front .brand { position: absolute; left: 0; right: 0; top: 92px; justify-content: center; }
  .front .brand__square { width: 78px; height: 78px; }
  .front .brand__name { font-size: 62px; }

  .details {
    position: absolute; left: 0; right: 0; bottom: 48px;
    display: flex; justify-content: center; align-items: flex-end;
    color: #fff;
  }
  .person { text-align: right; padding-right: 28px; border-right: 2px solid rgba(255,255,255,0.85); }
  .person__name { font-size: 30px; font-weight: 500; margin-bottom: 10px; }
  .person__line { font-size: 21px; line-height: 1.45; }
  .contact { padding-left: 28px; }
  .contact__line { font-size: 21px; line-height: 1.45; }
  .label { font-weight: 700; }

  .back { background: var(--paper); }
  .appointment__title {
    position: absolute; top: 92px; left: 0; right: 0; text-align: center;
    font-size: 25px; color: #7a7a7a; letter-spacing: 0.02em;
  }
  .appointment__fields {
    position: absolute; top: 168px; left: 62px; right: 62px;
    display: flex; align-items: flex-end; gap: 8px;
    font-size: 25px; color: #7a7a7a;
  }
  .blank { border-bottom: 2px dotted var(--line-grey); height: 26px; }
  .blank--day, .blank--month { width: 78px; }
  .blank--year { width: 86px; }
  .blank--time { flex: 1; }
  .field-gap { width: 28px; }
  .back .brand { position: absolute; right: 48px; bottom: 56px; gap: 12px; }
  .back .brand__square { width: 40px; height: 40px; }
  .back .brand__name { font-size: 30px; }
</style>
</head>
<body>
<main class="sheet">

  <section class="card front" aria-label="Business card front">
    <svg class="card__band" viewBox="0 0 800 488" preserveAspectRatio="none" aria-hidden="true">
      <path d="M0,262 Q360,236 800,158" fill="none" stroke="var(--swoosh-grey)" stroke-width="10"/>
      <path d="M0,274 Q360,248 800,170 L800,488 L0,488 Z" fill="var(--band-blue)"/>
    </svg>
    <div class="brand">
      <span class="brand__square"></span>
      <span class="brand__name">Gumlyssa</span>
    </div>
    <div class="details">
      <div class="person">
        <p class="person__name">Ravi Pelling</p>
        <p class="person__line">BDT, PGDipCDentTech Marlow</p>
        <p class="person__line">Dental Prosthetist</p>
        <p class="person__line"><span class="label">P:</span> 0800 47 2150, 09 571 3294</p>
      </div>
      <div class="contact">
        <p class="contact__line"><span class="label">E:</span> ravi@gumlyssa.co.nz</p>
        <p class="contact__line"><span class="label">W:</span> www.gumlyssa.co.nz</p>
        <p class="contact__line"><span class="label">A:</span> 418 Whiroa Road</p>
        <p class="contact__line">Kauriwhenua East, Auckland 0742</p>
      </div>
    </div>
  </section>

  <section class="card back" aria-label="Business card back">
    <p class="appointment__title">your next appointment</p>
    <div class="appointment__fields">
      <span>date</span>
      <span class="blank blank--day"></span><span>/</span>
      <span class="blank blank--month"></span><span>/</span>
      <span class="blank blank--year"></span>
      <span class="field-gap"></span>
      <span>time</span>
      <span class="blank blank--time"></span>
    </div>
    <div class="brand">
      <span class="brand__square"></span>
      <span class="brand__name">Gumlyssa</span>
    </div>
  </section>

</main>
</body>
</html>
```